Brisk Hollow Builders Needs A Flyer

We need a flyer for our newest product "The Cedarlane Garden Workroom"

Here is some copy for the flyer:

1. More and more people everyday are working from home and finding it difficult to disconnect from home activities in order to focus on their work. They are also finding it very expensive to add on to their existing house for a quiet place. Our archatectually stunning, Cedarlane Garden Workroom is the answer. The office studio measures 16' wide and 10' deep. 160 Square feet of space.

Perfect for dozens of purposes. Home office, design studio, artist studio, home school office, reading room, craft studio, drafting room.

Features include:

- Steel Framing. 40-60% lighter then wood, higher strength to weight ratio, resistant to mold and fire and steel is the most recycled material on earth!
- Spray foam insulation. Cool in the summer and warm in the winter.
- HVAC Mini Split with wireless remote control and thermostat.
- 100% Off grid with enough solar and battery storage to run your entire office. No need to pay for an expensive electric installation.
- Flush fitting floor outlets to reduce wires.
- TV mount (Optional with pre-wired electric, HDMI, digital audio & Cat 6)
- Windows are tempered glass custom made by Morvik Glazing.
- Solar qualifies for a 26% tax credit. This is not a write-off rather it is a direct reduction on your tax obligation.
- Thousands of dollars less than adding onto your home.
- Custom color, siding, features available.

This beautiful back yard office is delivered 100% assembled and ready to enjoy on the day of delivery.

We ship nationwide from our factory in South Carolina. Give us a call anytime to speak to a designer and start your dream office today!

555-318-4027
info@BriskHollowBuilders.example

```html
<!DOCTYPE html>
<html lang="en">
<head>
<meta charset="utf-8">
<title>The Cedarlane Garden Workroom – Brisk Hollow Builders</title>
<link rel="stylesheet" href="https://fonts.googleapis.com/css2?family=Montserrat:wght@800;900&family=Raleway:ital,wght@0,300;0,400;0,500;0,700;0,800;1,700;1,800&display=swap">
<style>
:root{
  --green:#5ba84b;
  --green-light:#64ab4f;
  --green-dark:#234a24;
  --orange:#eeaa2b;
  --ink:#4a4a4a;
  --list-ink:#5d5d62;
  --white:#ffffff;
  --stage:#d8d8da;
}
*{margin:0;padding:0;box-sizing:border-box}
html,body{width:930px;height:1200px;overflow:hidden;background:var(--stage)}
body{font-family:'Raleway',sans-serif;color:var(--ink)}
.flyer{position:absolute;left:40px;top:0;width:849px;height:1200px;background:var(--white);overflow:hidden}
.hero{position:absolute;left:0;top:0;width:849px;height:502px}
.hero-title{position:absolute;left:41px;top:96px;line-height:1}
.hero-title .light{display:block;font-weight:400;color:var(--white);font-size:47px;letter-spacing:1px;margin-bottom:4px}
.hero-title .accent{display:block;font-family:'Montserrat',sans-serif;font-weight:800;color:var(--orange);font-size:56px;margin-top:0}
.hero-title .heavy{display:block;font-family:'Montserrat',sans-serif;font-weight:900;color:var(--green);font-size:45px;margin-top:4px}
.intro{position:absolute;left:60px;width:729px;top:404px;text-align:center;color:var(--white);font-size:14.6px;line-height:18.8px;font-weight:400}
.product-view{position:absolute;left:43px;top:519px;width:338px;height:194px}
.uses-arrow{position:absolute;left:392px;top:543px}
.uses-lead{position:absolute;left:388px;top:598px;width:162px;text-align:center;color:var(--green);font-weight:800;font-style:italic;font-size:25px;line-height:35px}
.uses-list{position:absolute;left:565px;top:538px;list-style:none}
.uses-list li{position:relative;padding-left:23px;font-weight:800;font-style:italic;font-size:18.5px;line-height:24px;color:var(--list-ink);text-transform:uppercase}
.tick::before{content:"";position:absolute;left:0;width:12px;height:12px;border:1.4px solid currentColor;border-radius:50%}
.tick::after{content:"";position:absolute;left:4px;width:8px;height:4px;border-left:1.8px solid currentColor;border-bottom:1.8px solid currentColor;transform:rotate(-45deg)}
.uses-list li::before{top:6px}
.uses-list li::after{top:8px;left:4px}
.features-frame{position:absolute;left:63px;top:748px;width:722px;height:18px;border-top:1.6px solid var(--orange);border-left:1.6px solid var(--orange);border-right:1.6px solid var(--orange)}
.features-title{position:absolute;left:0;width:849px;top:733px;text-align:center}
.features-title span{background:var(--white);padding:0 14px;color:var(--orange);font-weight:700;font-size:26px;line-height:30px}
.features{position:absolute;top:772px;list-style:none}
.features.left{left:74px;width:334px}
.features.right{left:437px;width:338px}
.features li{position:relative;padding-left:22px;font-size:14.6px;line-height:19px;font-weight:400;color:var(--ink);text-align:justify}
.features li::before{top:6px}
.features li::after{top:8px;left:4px}
.delivery-band{position:absolute;left:0;top:994px;width:559px;height:126px;background:var(--green);color:var(--white);text-align:center}
.delivery-band .headline{margin-top:14px;font-weight:800;font-style:italic;font-size:16.6px;line-height:20.5px;letter-spacing:-0.3px}
.delivery-band .body{margin-top:9px;font-size:14.6px;line-height:16px}
.band-end{position:absolute;left:792px;top:994px;width:57px;height:126px;background:var(--green)}
.brand{position:absolute;left:559px;top:994px;width:233px;height:126px;display:flex;align-items:center;justify-content:center;gap:8px}
.brand .mark{width:14px;height:14px;border-radius:50%;background:var(--orange)}
.brand .name{font-weight:800;color:var(--orange);font-size:19px;line-height:22px;text-align:center}
.contact{position:absolute;left:0;top:1140px;width:849px;height:40px}
.contact svg{position:absolute;top:0}
.contact .value{position:absolute;top:2px;font-weight:800;font-style:italic;color:var(--green);line-height:36px}
.contact .phone{left:92px;font-size:28px}
.contact .email{left:373px;font-size:23.5px}
</style>
</head>
<body>
<main class="flyer">
  <svg class="hero" viewBox="0 0 849 502" width="849" height="502">
    <defs>
      <linearGradient id="yard" x1="0" y1="0" x2="0" y2="1">
        <stop offset="0" stop-color="#3f6f34"/>
        <stop offset="0.55" stop-color="#24461f"/>
        <stop offset="1" stop-color="#1d3a1a"/>
      </linearGradient>
      <linearGradient id="studio" x1="0" y1="0" x2="1" y2="0">
        <stop offset="0" stop-color="#4a4b4d"/>
        <stop offset="0.3" stop-color="#d9d3cb"/>
        <stop offset="0.7" stop-color="#e7e2da"/>
        <stop offset="1" stop-color="#3d3e40"/>
      </linearGradient>
      <clipPath id="heroClip"><rect x="0" y="0" width="849" height="366"/></clipPath>
    </defs>
    <rect x="0" y="0" width="849" height="366" fill="url(#yard)" role="img" aria-label="Evening garden with trees and a lawn behind the workroom"/>
    <g clip-path="url(#heroClip)">
      <circle cx="720" cy="330" r="305" fill="var(--green-light)" stroke="var(--white)" stroke-width="4"/>
    </g>
    <path d="M0 366 H430 C560 372 700 360 849 308 V502 H0 Z" fill="var(--orange)"/>
    <rect x="350" y="80" width="499" height="300" fill="url(#studio)" role="img" aria-label="Garden workroom with dark siding, full-height glass doors and a bright furnished interior"/>
  </svg>

  <h1 class="hero-title">
    <span class="light">THE</span>
    <span class="light">CEDARLANE</span>
    <span class="accent">Garden</span>
    <span class="heavy">WORKROOM</span>
  </h1>

  <p class="intro">More and more people everyday are working from home and finding it difficult to disconnect from home activities in order to focus on their work. They are also finding it very expensive to add on to their existing house for a quiet place. Our archatectually stunning, Cedarlane Garden Workroom is the answer. The office studio measures 16' wide and 10' deep. 160 Square feet of space.</p>

  <svg class="product-view" viewBox="0 0 338 194" role="img" aria-label="Front view of the workroom showing three glazed bays and a central double door">
    <defs>
      <linearGradient id="front" x1="0" y1="0" x2="0" y2="1">
        <stop offset="0" stop-color="#3e3f41"/>
        <stop offset="0.15" stop-color="#e4dfd8"/>
        <stop offset="1" stop-color="#cfc8bf"/>
      </linearGradient>
    </defs>
    <rect x="0" y="0" width="338" height="194" fill="url(#front)"/>
  </svg>

  <svg class="uses-arrow" width="120" height="60" viewBox="0 0 120 60" aria-hidden="true">
    <path d="M8 20 C40 4 70 0 88 10 C100 18 96 30 86 28 C74 26 80 10 96 14 C108 18 110 32 110 44" fill="none" stroke="var(--orange)" stroke-width="1.6" stroke-dasharray="5 4"/>
    <path d="M4 22 L14 14 L13 24 Z" fill="var(--orange)"/>
    <path d="M105 44 L115 44 L110 52 Z" fill="var(--orange)"/>
  </svg>

  <p class="uses-lead">Perfect for dozens of purposes.</p>

  <ul class="uses-list">
    <li class="tick">Home Office</li>
    <li class="tick">Design Studio</li>
    <li class="tick">Artist Studio</li>
    <li class="tick">Home School Office</li>
    <li class="tick">Reading Room</li>
    <li class="tick">Craft Studio</li>
    <li class="tick">Drafting Room</li>
  </ul>

  <div class="features-frame"></div>
  <h2 class="features-title"><span>FEATURES INCLUDE:</span></h2>

  <ul class="features left">
    <li class="tick">Steel Framing. 40-60% lighter then wood, higher strength to weight ratio, resistant to mold and fire and steel is the most recycled material on earth!</li>
    <li class="tick">Spray foam insulation. Cool in the summer and warm in the winter.</li>
    <li class="tick">HVAC Mini Split with wireless remote control and thermostat.</li>
    <li class="tick">100% Off grid with enough solar and battery storage to run your entire office. No need to pay for an expensive electric installation.</li>
  </ul>
  <ul class="features right">
    <li class="tick">Flush fitting floor outlets to reduce wires.</li>
    <li class="tick">TV mount (Optional with pre-wired electric, HDMI, digital audio &amp; Cat 6)</li>
    <li class="tick">Windows are tempered glass custom made by Morvik Glazing.</li>
    <li class="tick">Solar qualifies for a 26% tax credit. This is not a write-off rather it is a direct reduction on your tax obligation.</li>
    <li class="tick">Thousands of dollars less than adding onto your home.</li>
    <li class="tick">Custom color, siding, features available.</li>
  </ul>

  <section class="delivery-band">
    <p class="headline">This beautiful back yard office is delivered 100%<br>assembled and ready to enjoy on the day of delivery.</p>
    <p class="body">We ship nationwide from our factory in South Carolina.<br>Give us a call anytime to speak to a designer and<br>start your dream office today!</p>
  </section>
  <div class="brand"><span class="mark"></span><span class="name">Brisk Hollow<br>Builders</span></div>
  <div class="band-end"></div>

  <footer class="contact">
    <svg style="left:40px" width="40" height="40" viewBox="0 0 40 40" aria-hidden="true">
      <path d="M9 6 L15 5 L18 13 L14 16 C16 21 19 24 24 26 L27 22 L35 25 L34 31 C32 35 27 36 22 34 C14 30 9 25 6 18 C4 13 5 8 9 6 Z" fill="none" stroke="var(--orange)" stroke-width="1.8" stroke-linejoin="round"/>
      <path d="M24 9 A8 8 0 0 1 31 16 M25 4 A13 13 0 0 1 36 15" fill="none" stroke="var(--orange)" stroke-width="1.8"/>
    </svg>
    <span class="value phone">555-318-4027</span>
    <svg style="left:324px;top:-3px" width="40" height="42" viewBox="0 0 40 42" aria-hidden="true">
      <path d="M3 17 L20 3 L37 17 V38 H3 Z" fill="none" stroke="var(--orange)" stroke-width="1.8" stroke-linejoin="round"/>
      <path d="M3 17 L20 29 L37 17 M3 38 L16 26 M37 38 L24 26" fill="none" stroke="var(--orange)" stroke-width="1.8"/>
    </svg>
    <span class="value email">info@BriskHollowBuilders.example</span>
  </footer>
</main>
</body>
</html>
```